all sorted property services

Target Market(s)

General letter head for emails and letter quotes ect

Colors
0054AA
0677BA
7BADD7
CADEEF
E8F1F8
0094D4
00A9DD
6FCCEA
C7EBF8
E9F6FB

Requirements
Must have
• logo phone email website names
Nice to have
• what we do (from the website)

```html
<!DOCTYPE html>
<html lang="en">
<head>
<meta charset="utf-8">
<title>All Sorted Property Services – Letterhead</title>
<link href="https://fonts.googleapis.com/css2?family=Montserrat:wght@400;500;600;700&display=swap" rel="stylesheet">
<style>
  :root{
    --navy:#1e3a8a;
    --deep-blue:#0054AA;
    --sky:#0094D4;
    --cyan:#00A9DD;
    --ink:#111111;
    --text:#333a45;
    --body-grey:#8a8f96;
    --rule:#e2e4e8;
    --mark:#eeeff1;
    --backdrop:#eceef0;
    --paper:#ffffff;
  }
  *{box-sizing:border-box;margin:0;padding:0}
  html,body{width:999px;height:1200px;overflow:hidden}
  body{background:var(--backdrop);font-family:"Montserrat",sans-serif;position:relative}
  .letterhead{position:absolute;left:100px;top:40px;width:800px;height:1120px;background:var(--paper);overflow:hidden}

  .brand{position:absolute;left:72px;top:60px;display:flex;align-items:center;gap:14px}
  .brand-dot{width:46px;height:46px;border-radius:50%;background:var(--deep-blue);flex:none}
  .brand-name{font-weight:700;font-size:20px;line-height:1.2;color:var(--navy);text-transform:uppercase;letter-spacing:.5px}

  .contact-list{position:absolute;left:564px;top:58px;list-style:none}
  .contact-list li{display:flex;align-items:flex-start;gap:7px;font-size:11px;color:#555b63;line-height:1.3;margin-bottom:10px}
  .contact-list li:first-child{margin-bottom:16px}
  .icon{flex:none;width:14px;height:14px;border-radius:3px;display:flex;align-items:center;justify-content:center}
  .icon svg{width:10px;height:10px}
  .icon.navy{background:var(--navy)}
  .icon.sky{background:var(--sky)}

  .header-rule{position:absolute;left:59px;top:218px;width:681px;height:2px;background:var(--rule)}

  .recipient{position:absolute;left:73px;top:300px}
  .recipient-name{font-weight:700;font-size:19px;color:var(--navy);letter-spacing:.3px;margin-bottom:8px}
  .recipient p{font-size:13px;font-weight:500;color:var(--text);line-height:1.35;margin-bottom:8px}

  .letter-date{position:absolute;right:72px;top:405px;font-size:15px;font-weight:500;color:#4a4f57}

  .letter-body{position:absolute;left:73px;top:448px;width:655px}
  .letter-body p{font-size:13.6px;line-height:23.5px;color:var(--body-grey);text-align:justify;margin-bottom:24px}

  .signoff{position:absolute;left:73px;top:758px;font-weight:600;font-size:23px;color:var(--ink)}
  .signature{position:absolute;left:108px;top:800px;width:120px;height:72px;background:linear-gradient(120deg,#f2f2f2,#e6e6e6);border-radius:4px}

  .footer-mark{position:absolute;left:430px;top:880px;width:340px;height:340px;border-radius:50%;background:var(--mark)}

  .footer-band{position:absolute;left:0;top:997px;width:432px;height:84px;background:linear-gradient(90deg,var(--sky),var(--navy));clip-path:polygon(0 0,100% 0,96% 100%,0 100%);display:flex;gap:30px;padding:10px 0 0 40px;color:#fff}
  .footer-band ul{list-style:none}
  .footer-band li{display:flex;align-items:flex-start;gap:7px;font-size:11px;font-weight:500;line-height:1.35;margin-bottom:6px}
  .footer-band .icon{background:#fff}
</style>
</head>
<body>
<main class="letterhead">
  <header>
    <div class="brand">
      <span class="brand-dot"></span>
      <span class="brand-name">All Sorted<br>Property Services</span>
    </div>
    <ul class="contact-list">
      <li><span class="icon navy"><svg viewBox="0 0 10 10"><path d="M5 1a3 3 0 0 0-3 3c0 2.2 3 5 3 5s3-2.8 3-5a3 3 0 0 0-3-3z" fill="#fff"/><circle cx="5" cy="4" r="1" fill="#1e3a8a"/></svg></span><span>2710 Harbor Lane<br>Fairview, OR 97024</span></li>
      <li><span class="icon sky"><svg viewBox="0 0 10 10"><path d="M2 1.5l2 .3.6 2-1 .8a5 5 0 0 0 2 2l.8-1 2 .6.3 2C6 8.5 1.5 4 2 1.5z" fill="#fff"/></svg></span><span>+00 555 204 18</span></li>
      <li><span class="icon sky"><svg viewBox="0 0 10 10"><rect x="1" y="2.5" width="8" height="5.5" rx=".6" fill="#fff"/><path d="M1.3 3l3.7 2.6L8.7 3" stroke="#0094D4" stroke-width=".8" fill="none"/></svg></span><span>hello@allsortedps.com</span></li>
      <li><span class="icon sky"><svg viewBox="0 0 10 10"><path d="M2.5 1.5l5 3.5-2.2.4 1.2 2.5-1 .5-1.2-2.5-1.8 1.5z" fill="#fff"/></svg></span><span>www.allsortedps.com</span></li>
    </ul>
    <div class="header-rule"></div>
  </header>

  <section class="recipient">
    <h2 class="recipient-name">DANA WHITFIELD</h2>
    <p>0555-218-437</p>
    <p>dana@whitfieldmail.com</p>
    <p>88 Maple Row Suite<br>4 Austin, TX 0000</p>
  </section>

  <p class="letter-date">12 December, 2024</p>

  <section class="letter-body">
    <p>Lorem ipsum dolor sit amet, consectetuer adipiscing elit, sed diam nonummy nibh euismod tincidunt ut laoreet dolore magna aliquam erat volutpat. Ut wisi enim ad minim veniam, quis nostrud exerci tation ullamcorper suscipit lobortis nisl ut aliquip ex ea commodo consequat. Duis autem vel eum iriure dolor in hendrerit in vulputate velit esse molestie consequat, vel illum dolore eu feugiat nulla facilisis at vero eros et accumsan et iusto odio dignissim qui blandit praesent luptatum zzril delenit augue duis dolore te feugait nulla facilisi.</p>
    <p>Lorem ipsum dolor sit amet, cons ectetuer adipiscing elit, sed diam nonummy nibh euismod tincidunt ut laoreet dolore magna aliquam erat volutpat. Ut wisi enim ad minim veniam, quis nostrud exerci tation ullamcorper suscipit lobortis nisl ut aliquip ex ea commodo consequat.</p>
  </section>

  <p class="signoff">Mr. Dana Whitfield</p>
  <div class="signature" role="img" aria-label="Handwritten signature of Dana Whitfield"></div>

  <div class="footer-mark"></div>

  <footer class="footer-band">
    <ul>
      <li><span class="icon"><svg viewBox="0 0 10 10"><path d="M2 1.5l2 .3.6 2-1 .8a5 5 0 0 0 2 2l.8-1 2 .6.3 2C6 8.5 1.5 4 2 1.5z" fill="#0094D4"/></svg></span>+00 555 204 18</li>
      <li><span class="icon"><svg viewBox="0 0 10 10"><rect x="1" y="2.5" width="8" height="5.5" rx=".6" fill="#0094D4"/><path d="M1.3 3l3.7 2.6L8.7 3" stroke="#fff" stroke-width=".8" fill="none"/></svg></span>hello@allsortedps.com</li>
      <li><span class="icon"><svg viewBox="0 0 10 10"><path d="M2.5 1.5l5 3.5-2.2.4 1.2 2.5-1 .5-1.2-2.5-1.8 1.5z" fill="#0094D4"/></svg></span>www.allsortedps.com</li>
    </ul>
    <ul>
      <li><span class="icon"><svg viewBox="0 0 10 10"><path d="M5 1a3 3 0 0 0-3 3c0 2.2 3 5 3 5s3-2.8 3-5a3 3 0 0 0-3-3z" fill="#0054AA"/><circle cx="5" cy="4" r="1" fill="#fff"/></svg></span><span>2710 Harbor<br>Lane Fairview,<br>OR 97024</span></li>
    </ul>
  </footer>
</main>
</body>
</html>
```